Pixagram Business Card For Comedian

Hi,

I'd like a 2-sided business card that kind mimics an Pixagram page. I've attached screenshots with the copy and language that should be written on there.

I'd like it to be way more stylized and a bit more creative than what I did on Powerpoint. I just did a mockup so that you can have an idea. I'd like it to be designed and you to take a bit of creative imagery so that it doesn't look so static and monochromatic.

PLEASE BE CREATIVE WITH THESE DESIGNS. I DON'T WANT IT TO LOOK EXACTLY LIKE THE ATTACHED IMAGE OR EXACTLY LIKE AN PIXAGRAM PAGE. I want to use it as inspiration to create something that looks more sleek, and creative. I don't want the colors to just be boring gray, and blue. Have fun and spice it up a bit!

Check out my website DanaWellmore.com to see the colors and fonts I use for my branding.

For the main photo: Here's a link with the hi-res photo: !https://www.filecrate.example/s/q8wtm3hzr5bdk2p/Dana-Wellmore-C71F2254.jpg?dl=0

For the thumbnail icon photo, you can use this: https://www.filecrate.example/s/vn4rx9kplw2tjdm/Dana%20Wellmore%20Glass%20Yard%20Headshot.jpg?dl=0

Use the Standard Business Card Template from Plinx.com:
https://help.plinx.example/hc/en-us/article_attachments/318274905/Standard_Size__US__Business_Cards_Portrait.jpg

Please let me know if you have any questions.
Updates

Industry/Entity Type

Business

Contact Information for Business Card

All of the text and copy has been provided on the attached jpg.

Colors
33a6d7
0255a3
aaaaaa
dbdbdb
1b1b1b

Requirements
Should not have
• A Hyperlink for the Email Addresses

```html
<!DOCTYPE html>
<html lang="en">
<head>
<meta charset="utf-8">
<title>Dana Wellmore — Business Card</title>
<link href="https://fonts.googleapis.com/css2?family=Roboto:wght@400;500&family=Roboto+Condensed:wght@400&display=swap" rel="stylesheet">
<style>
  :root{
    --bg:#eef1f1;
    --card:#ffffff;
    --ink:#1b1b1b;
    --label:#aaaaaa;
    --rule:#dbdbdb;
    --sky:#33a6d7;
    --navy:#0255a3;
    --link:#2a3fb0;
    --heart:#e8253b;
  }
  *{box-sizing:border-box;margin:0;padding:0}
  html,body{width:1200px;height:1066px;overflow:hidden;background:var(--bg);font-family:"Roboto",Arial,sans-serif;color:var(--ink)}
  .card{position:absolute;top:165px;width:420px;height:735px;background:var(--card);box-shadow:0 18px 40px rgba(0,0,0,.08);overflow:hidden}
  .card--profile{left:150px}
  .card--post{left:630px}

  /* profile side */
  .card--profile{display:flex;flex-direction:column;padding:112px 40px 40px}
  .profile__avatar{position:absolute;top:34px;right:34px;width:130px;height:130px;border-radius:50%;background:radial-gradient(circle at 50% 40%,#6a4634,#2a1a14 70%)}
  .profile__fields{display:flex;flex-direction:column}
  .field{padding:10px 0;border-bottom:1px solid var(--rule)}
  .field:last-child{border-bottom:none}
  .field--name{padding-right:150px}
  .field__label{font-size:13px;line-height:16px;color:var(--label);margin-bottom:4px}
  .field__value{font-size:15px;line-height:21px;color:var(--ink)}
  .field__value + .field__value{margin-top:6px}
  .field__note{margin-top:10px}
  .socials{margin-top:18px}
  .socials__label{font-size:13px;line-height:16px;color:var(--label);margin-bottom:12px}
  .social{display:flex;align-items:center;gap:12px;font-size:15px;line-height:21px;margin-bottom:12px}
  .social:last-child{margin-bottom:0}
  .social__dot{width:30px;height:30px;border-radius:50%;flex:none}
  .social__name{font-size:11px;color:var(--label);margin-left:4px}
  .social--faceroll .social__dot{background:var(--navy)}
  .social--chirpr .social__dot{background:var(--sky)}
  .social--pixagram .social__dot{border:2px solid var(--label)}

  /* post side */
  .post__header{height:80px;display:flex;align-items:center;padding:0 22px;gap:12px}
  .post__avatar{width:36px;height:36px;border-radius:50%;background:radial-gradient(circle at 50% 40%,#6a4634,#2a1a14 70%)}
  .post__handle{font-size:16px;font-weight:500}
  .post__place{margin-left:auto;font-size:13px;color:var(--link)}
  .post__photo{height:460px;background:linear-gradient(180deg,#efe6e2 0%,#2a1d19 22%,#5a3526 48%,#e65c74 78%,#f0708a 100%)}
  .post__likes{display:flex;align-items:center;gap:8px;padding:16px 22px 8px;font-size:11px;color:var(--link);text-transform:uppercase;letter-spacing:.02em}
  .post__caption{padding:0 22px;font-family:"Roboto Condensed",Arial,sans-serif;font-size:13px;line-height:1.4;text-transform:uppercase}
  .post__caption strong{font-family:"Roboto",Arial,sans-serif;font-weight:500;text-transform:none;font-size:15px}
  .post__caption .lead{text-transform:none}
</style>
</head>
<body>

<section class="card card--profile">
  <div class="profile__avatar" role="img" aria-label="Round headshot thumbnail of the comedian"></div>
  <div class="profile__fields">
    <div class="field field--name">
      <p class="field__label">Name</p>
      <p class="field__value">Dana Wellmore</p>
    </div>
    <div class="field">
      <p class="field__label">Website</p>
      <p class="field__value">www.danawellmore.com</p>
    </div>
    <div class="field">
      <p class="field__label">Bookings</p>
      <p class="field__value">Krista@NorthlineTalent.com</p>
      <p class="field__value">jo.halvers@bcmgmt.com</p>
    </div>
    <div class="field">
      <p class="field__label">About</p>
      <p class="field__value">Stand up comedian. I host. I write. I act. I don't sing unless I'm in the shower. I accept tips for my jokes (but on Paywave).</p>
      <p class="field__value field__note">As seen on Northlight, Punchline TV, Mixwave, Tempo.</p>
    </div>
  </div>
  <div class="socials">
    <p class="socials__label">More info</p>
    <div class="social social--faceroll"><span class="social__dot"></span>/danawellmore<span class="social__name">Faceroll</span></div>
    <div class="social social--chirpr"><span class="social__dot"></span>/wellfab<span class="social__name">Chirpr</span></div>
    <div class="social social--pixagram"><span class="social__dot"></span>/wellfab<span class="social__name">Pixagram</span></div>
  </div>
</section>

<section class="card card--post">
  <header class="post__header">
    <div class="post__avatar" role="img" aria-label="Small round profile headshot"></div>
    <span class="post__handle">wellfab</span>
    <span class="post__place">Brooklyn, New York</span>
  </header>
  <div class="post__photo" role="img" aria-label="Portrait photo of the comedian with curly hair in a pink top"></div>
  <div class="post__likes">
    <svg width="16" height="14" viewBox="0 0 16 14" aria-hidden="true"><path d="M8 14 1.2 7.2A4 4 0 0 1 8 2a4 4 0 0 1 6.8 5.2Z" fill="var(--heart)"/></svg>
    Everybody loves me
  </div>
  <p class="post__caption"><strong>wellfab</strong> <span class="lead">Your favorite comic's favorite comic.</span> #ISAIDIT #SOITSTRUE #FINDME #FOLLOWME #NOTTOMYHOUSE #POSTABOUTMEUSINGTHESEHASHTAGS #DANAWELLMORE #WELLFAB #IMSUCHABROOKLYNGIRL #MAKENYUNSAFEAGAIN #BROOKLYNSTANDUPCOMEDY</p>
</section>

</body>
</html>
```